Stationery and Business Card Design

We need stationary design for our new company pelvanta. Pelvanta is a company that provides city apartment rentals for tourists in Athens We need business cards, letterheads for A4 and A5 and envelopes for A4 A5. The design needs to be modern, friendly and corporate.

Target Market(s)

City Tourists

Industry/Entity Type

Tourism

```html
<!DOCTYPE html>
<html lang="en">
<head>
<meta charset="utf-8">
<title>Pelvanta – Envelope Dieline</title>
<link rel="stylesheet" href="https://fonts.googleapis.com/css2?family=Montserrat:wght@400;500&display=swap">
<style>
  :root {
    --brand-magenta: #95205c;
    --paper: #ffffff;
    --die-line: #3a3136;
    --die-line-soft: #6d6d6d;
    --fold-line: #8a8a8a;
    --crop-mark: #2b2b2b;
    --ink: #3b3b3b;
  }
  html, body {
    margin: 0;
    padding: 0;
    width: 1200px;
    height: 1200px;
    overflow: hidden;
    background: var(--paper);
  }
  .sheet {
    display: block;
    width: 1200px;
    height: 1200px;
  }
  .crop-marks line { stroke: var(--crop-mark); stroke-width: 1.5; }
  .crop-marks .dash { stroke-width: 1.2; }
  .inside-fill { fill: var(--brand-magenta); }
  .die-cut { fill: none; stroke: var(--die-line); stroke-width: 2; stroke-linejoin: round; }
  .die-cut--front { stroke: var(--die-line-soft); fill: var(--paper); }
  .fold { fill: none; stroke: var(--fold-line); stroke-width: 1.5; stroke-dasharray: 8 5; }
  .brand-mark { fill: var(--brand-magenta); }
  .brand-name {
    font-family: "Montserrat", sans-serif;
    font-weight: 500;
    font-size: 11px;
    fill: var(--brand-magenta);
  }
  .return-address {
    font-family: "Montserrat", sans-serif;
    font-weight: 400;
    font-size: 4.6px;
    fill: var(--ink);
  }
</style>
</head>
<body>
<svg class="sheet" viewBox="0 0 1200 1200" xmlns="http://www.w3.org/2000/svg">

  <!-- Inside print: full magenta -->
  <g class="envelope envelope--inside">
    <rect class="inside-fill" x="339" y="143" width="503" height="406"/>
    <path class="inside-fill" d="M381 142 L392 104 Q396 95 408 95 L772 95 Q786 95 790 106 L800 142 Z"/>
    <path class="die-cut" d="M368 142 L379 100 Q384 84 402 84 L778 84 Q796 84 801 100 L812 142 L830 148 Q832 150 832 156 L832 346 Q832 349 829 350 L813 356 L805 538 L377 538 L368 356 L351 350 Q348 349 348 346 L348 156 Q348 150 351 148 Z"/>
  </g>

  <!-- Outside print: white with branding -->
  <g class="envelope envelope--outside">
    <path class="die-cut die-cut--front" d="M368 699 L379 657 Q384 641 402 641 L778 641 Q796 641 801 657 L812 699 L830 705 Q832 707 832 713 L832 903 Q832 906 829 907 L813 913 L805 1096 L377 1096 L368 913 L351 907 Q348 906 348 903 L348 713 Q348 707 351 705 Z"/>
    <rect class="fold" x="368" y="700" width="445" height="213"/>

    <g class="brand-lockup">
      <rect class="brand-mark" x="406" y="722" width="14" height="14"/>
      <text class="brand-name" x="390" y="748">pelvanta</text>
    </g>

    <g class="return-address" transform="rotate(180 690 945)">
      <text x="590" y="926">Pelvanta</text>
      <text x="590" y="933">Ermou 42, Plaka, Athens 105 56, Attica, Greece</text>
      <text x="590" y="940">T. +30 210 555 0142 | F. +30 210 555 0143 | E. stay@pelvanta.example</text>
      <text x="590" y="953">www.pelvanta.example</text>
    </g>
  </g>

  <!-- Crop and registration marks -->
  <g class="crop-marks">
    <line x1="349" y1="40" x2="349" y2="62"/><line class="dash" x1="367" y1="42" x2="367" y2="48"/><line class="dash" x1="367" y1="54" x2="367" y2="62"/>
    <line x1="832" y1="40" x2="832" y2="62"/><line class="dash" x1="814" y1="42" x2="814" y2="48"/><line class="dash" x1="814" y1="54" x2="814" y2="62"/>
    <line x1="305" y1="84" x2="327" y2="84"/><line x1="853" y1="84" x2="876" y2="84"/>
    <line class="dash" x1="305" y1="142" x2="313" y2="142"/><line class="dash" x1="320" y1="142" x2="327" y2="142"/>
    <line class="dash" x1="853" y1="142" x2="861" y2="142"/><line class="dash" x1="869" y1="142" x2="876" y2="142"/>
    <line class="dash" x1="305" y1="354" x2="313" y2="354"/><line class="dash" x1="320" y1="354" x2="327" y2="354"/>
    <line class="dash" x1="853" y1="354" x2="861" y2="354"/><line class="dash" x1="869" y1="354" x2="876" y2="354"/>
    <line x1="305" y1="538" x2="327" y2="538"/><line x1="853" y1="538" x2="876" y2="538"/>
    <line x1="349" y1="560" x2="349" y2="582"/><line x1="832" y1="560" x2="832" y2="582"/>

    <line x1="349" y1="598" x2="349" y2="620"/><line class="dash" x1="367" y1="600" x2="367" y2="606"/><line class="dash" x1="367" y1="612" x2="367" y2="620"/>
    <line x1="832" y1="598" x2="832" y2="620"/><line class="dash" x1="814" y1="600" x2="814" y2="606"/><line class="dash" x1="814" y1="612" x2="814" y2="620"/>
    <line x1="305" y1="641" x2="327" y2="641"/><line x1="853" y1="641" x2="876" y2="641"/>
    <line class="dash" x1="305" y1="699" x2="313" y2="699"/><line class="dash" x1="320" y1="699" x2="327" y2="699"/>
    <line class="dash" x1="853" y1="699" x2="861" y2="699"/><line class="dash" x1="869" y1="699" x2="876" y2="699"/>
    <line class="dash" x1="305" y1="912" x2="313" y2="912"/><line class="dash" x1="320" y1="912" x2="327" y2="912"/>
    <line class="dash" x1="853" y1="912" x2="861" y2="912"/><line class="dash" x1="869" y1="912" x2="876" y2="912"/>
    <line x1="305" y1="1096" x2="327" y2="1096"/><line x1="853" y1="1096" x2="876" y2="1096"/>
    <line x1="349" y1="1118" x2="349" y2="1140"/><line class="dash" x1="367" y1="1120" x2="367" y2="1126"/><line class="dash" x1="367" y1="1132" x2="367" y2="1140"/>
    <line x1="832" y1="1118" x2="832" y2="1140"/><line class="dash" x1="814" y1="1120" x2="814" y2="1126"/><line class="dash" x1="814" y1="1132" x2="814" y2="1140"/>
  </g>
</svg>
</body>
</html>
```